Need a solid log.
My company Sales: OrbiCast, Halcyon Beam, Vorlan Internet
Design and installation of WI_FI systems.
Fulfillment company for installations in the Electronics industry

Industry/Entity Type

Electronics

Contact Information for Business Card

Peter R. Hollowell
President
Phone: 479.555.0182 Cell: 479.5550947 prhollowell@brightharbornet.biz
Bright Harbor Networks
Marlow Ridge, AL. 35990

```html
<!DOCTYPE html>
<html lang="en">
<head>
<meta charset="utf-8">
<title>Bright Harbor Networks – Business Card</title>
<link rel="stylesheet" href="https://fonts.googleapis.com/css2?family=Archivo+Black&family=Gelasio:wght@400;500;600&display=swap">
<style>
  :root {
    --backdrop: #6e3a1c;
    --card: #ffffff;
    --brand-green: #6cce2f;
    --ink: #111111;
    --ink-soft: #444444;
    --logo-ink: #ffffff;
  }
  * { margin: 0; padding: 0; box-sizing: border-box; }
  html, body {
    width: 1200px;
    height: 900px;
    overflow: hidden;
  }
  body {
    position: relative;
    background: var(--backdrop);
    font-family: "Gelasio", Georgia, serif;
    color: var(--ink);
  }
  .card {
    position: absolute;
    left: 418px;
    top: 140px;
    width: 363px;
    height: 618px;
    background: var(--card);
    text-align: center;
  }
  .brand-band {
    height: 200px;
    background: var(--brand-green);
    display: flex;
    flex-direction: column;
    justify-content: center;
    align-items: center;
    padding-top: 6px;
  }
  .brand-name {
    font-family: "Archivo Black", "Arial Black", sans-serif;
    font-weight: 400;
    color: var(--logo-ink);
    font-size: 40px;
    line-height: 47px;
    letter-spacing: 3px;
    text-transform: uppercase;
  }
  .brand-name span { display: block; }
  .services {
    margin-top: 10px;
    font-size: 14px;
    line-height: 22px;
  }
  .services .divider { margin: 0 6px; }
  .mission {
    margin-top: 3px;
    font-size: 14px;
    line-height: 18px;
    color: var(--ink-soft);
  }
  .person { margin-top: 66px; }
  .person-name { font-size: 19px; line-height: 24px; }
  .person-title { font-size: 16px; line-height: 22px; font-weight: 600; }
  .contact {
    margin-top: 68px;
    font-size: 14.5px;
    line-height: 19px;
    font-weight: 600;
  }
  .contact .location { margin-bottom: 19px; }
  .contact .email { margin-top: 18px; }
</style>
</head>
<body>
  <article class="card">
    <header class="brand-band">
      <h1 class="brand-name"><span>Bright</span><span>Harbor</span><span>Networks</span></h1>
    </header>

    <p class="services">OrbiCast<span class="divider">|</span>Halcyon Beam<span class="divider">|</span>Vorlan Internet<br>Design and Installation of WIFI systems</p>
    <p class="mission">Fulfillment company for installations<br>in the Electronics Industry</p>

    <div class="person">
      <p class="person-name">Peter R. Hollowell</p>
      <p class="person-title">President</p>
    </div>

    <div class="contact">
      <p class="location">Marlow Ridge, AL. 35990</p>
      <p class="phone">Phone: 479.555.0182</p>
      <p class="cell">Cell: 479.5550947</p>
      <p class="email">prhollowell@brightharbornet.biz</p>
    </div>
  </article>
</body>
</html>
```